Dog Grass Website

We need a two page website for our new product that will be shipped to customers of a tray with grass inside for a pet to relieve themselves. We are hoping for a clean look that translates a positive and upscale message.

The first page will be informative about the product and the second page will be 'about us'.

For more information please download the files. We have attached a screenshot of what the product box will look like

Gathering more feedback

```html
<!DOCTYPE html>
<html lang="en">
<head>
<meta charset="utf-8">
<title>PawPatch Turf</title>
<link href="https://fonts.googleapis.com/css2?family=Lato:wght@400;700&display=swap" rel="stylesheet">
<style>
  :root {
    --brown: #5a1f08;
    --green: #6cbf45;
    --green-soft: #b8e3a0;
    --green-pale: #d3efc2;
    --mint: #eafddf;
    --grey: #6b6b6b;
    --white: #ffffff;
    --field: #ececec;
  }
  * { box-sizing: border-box; margin: 0; padding: 0; }
  html, body { width: 717px; height: 1200px; overflow: hidden; }
  body { font-family: "Lato", sans-serif; background: var(--white); position: relative; color: var(--brown); }
  .page-bg { position: absolute; left: 0; top: 0; width: 717px; height: 954px; background: var(--mint); }
  .hero-shape { position: absolute; left: 0; top: 0; }
  .abs { position: absolute; }

  .brand { display: flex; align-items: center; gap: 6px; font-weight: 700; color: var(--brown); font-size: 22px; }
  .brand-dot { width: 14px; height: 14px; border-radius: 50%; background: var(--green); }

  .nav { top: 21px; left: 516px; display: flex; gap: 30px; font-size: 14px; }
  .nav a { color: var(--brown); text-decoration: none; padding-bottom: 5px; }
  .nav a.active { border-bottom: 1px solid #d9534f; }

  .hero-title { left: 103px; top: 152px; font-size: 17.5px; font-weight: 400; }
  .hero-sub { left: 103px; top: 187px; font-size: 15.5px; line-height: 19.5px; color: var(--grey); }
  .btn-info { left: 104px; top: 245px; width: 107px; height: 35px; border-radius: 18px; background: var(--green); color: var(--white); font-size: 13.5px; display: flex; align-items: center; justify-content: center; }

  .photo { background: linear-gradient(180deg, #9fcf86 0%, #5e9a3c 70%, #3e6e25 100%); }
  .hero-photo { left: 348px; top: 58px; width: 369px; height: 282px; border-radius: 8px 0 0 8px;
    background: linear-gradient(180deg, rgba(0,0,0,0) 0%, rgba(0,0,0,0) 55%, #4f8f2c 60%, #2f5a1a 100%); }

  .pup-blob { left: 104px; top: 432px; width: 234px; height: 233px; border-radius: 45% 55% 50% 45% / 40% 45% 60% 55%; background: var(--green-soft); }
  .pup-photo { left: 122px; top: 455px; width: 140px; height: 198px; border-radius: 48% 48% 18% 18%; background: radial-gradient(circle at 50% 40%, #f6ebcf, #e6cf9e 70%, #d8b57c); }
  .bubble { left: 239px; top: 415px; width: 102px; height: 75px; border-radius: 50%; background: var(--green); color: var(--white); font-size: 13px; line-height: 16px; text-align: right; padding: 25px 14px 0 0; }
  .bubble-tail { left: 263px; top: 488px; width: 9px; height: 9px; border-radius: 50%; background: var(--green); }

  .about-text { left: 367px; top: 448px; width: 260px; font-size: 13px; line-height: 18.8px; color: #3a3a3a; }

  .feature { top: 583px; width: 70px; text-align: center; font-size: 9.7px; line-height: 12px; color: var(--brown); }
  .feature svg { display: block; margin: 0 auto 7px; }

  .vet { left: 0; width: 717px; top: 710px; text-align: center; font-size: 22px; font-weight: 700; }
  .made { left: 302px; top: 745px; font-size: 17px; color: var(--grey); }
  .flag { left: 376px; top: 747px; width: 36px; height: 18px; background: linear-gradient(180deg, #b22234 0 14%, #fff 14% 28%, #b22234 28% 42%, #fff 42% 57%, #b22234 57% 71%, #fff 71% 85%, #b22234 85%); }

  .order { top: 820px; width: 244px; height: 70px; border-radius: 35px; background: var(--brown); color: var(--white); font-size: 17.5px; display: flex; flex-direction: column; align-items: center; justify-content: center; }
  .order small { font-size: 11px; font-weight: 700; margin-top: 2px; }
  .or { left: 346px; top: 847px; font-size: 17.5px; color: var(--green); font-weight: 700; }

  .seal { left: 328px; top: 930px; width: 62px; height: 48px; border-radius: 50%; background: #c8d34a; border: 2px solid var(--brown); }

  .footer-brand { left: 110px; top: 1030px; }
  .social { top: 1078px; width: 21px; height: 21px; border-radius: 50%; background: var(--brown); }
  .foot-head { top: 1020px; font-size: 11.6px; font-weight: 700; }
  .foot-links { left: 299px; top: 1043px; list-style: none; font-size: 7.3px; line-height: 13.5px; color: #333; }
  .news-text { left: 429px; top: 1043px; font-size: 7.6px; color: #333; }
  .email { left: 427px; top: 1075px; width: 186px; height: 25px; border-radius: 13px; background: var(--field); font-size: 7px; color: #999; padding: 8px 0 0 11px; }
  .subscribe { left: 551px; top: 1078px; width: 58px; height: 19px; border-radius: 10px; background: var(--green); color: var(--white); font-size: 7px; display: flex; align-items: center; justify-content: center; }
  .rule { left: 99px; top: 1138px; width: 519px; height: 1px; background: #e3e3e3; }
  .copyright { left: 0; width: 717px; top: 1158px; text-align: center; font-size: 10px; color: var(--grey); }
</style>
</head>
<body>
  <div class="page-bg"></div>
  <svg class="hero-shape" width="717" height="420" viewBox="0 0 717 420">
    <path d="M300,0 C330,60 325,130 325,210 C325,330 390,398 510,397 C610,396 690,365 717,350 L717,0 Z" fill="#d3efc2"/>
    <path d="M215,0 C290,40 330,110 335,200 C340,300 390,368 500,368 C600,368 680,345 717,335 L717,0 Z" fill="#b8e3a0"/>
  </svg>

  <div class="abs brand" style="left:103px;top:34px;"><span class="brand-dot"></span>PawPatch Turf</div>
  <nav class="abs nav"><a class="active" href="#">Shop</a><a href="#">About</a></nav>

  <h1 class="abs hero-title">Farm Fresh for your Furry Friend!</h1>
  <p class="abs hero-sub">Tray with grass inside<br>for a pet to relieve themselves</p>
  <div class="abs btn-info">more info</div>
  <div class="abs hero-photo" role="img" aria-label="Photo of a small black and white dog sitting on a tray of green grass"></div>

  <div class="abs pup-blob"></div>
  <div class="abs pup-photo" role="img" aria-label="Photo of a happy golden retriever puppy"></div>
  <div class="abs bubble">buy it for me<br>please!</div>
  <div class="abs bubble-tail"></div>

  <p class="abs about-text">This is a product for a pet parent on-the-go, living in an apartment where this would be a convenient solution. This could be useful in times of bad weather, when it is snowing outside, a dog will still have the natural grass available.</p>

  <div class="abs feature" style="left:352px;">
    <svg width="42" height="42" viewBox="0 0 42 42"><circle cx="21" cy="21" r="21" fill="#6cbf45"/><path d="M13,28 C13,18 20,13 29,13 C29,22 24,28 13,28 Z M13,28 L24,18" fill="none" stroke="#fff" stroke-width="1.5"/></svg>
    Natural<br>Grass</div>
  <div class="abs feature" style="left:420px;">
    <svg width="42" height="42" viewBox="0 0 42 42"><circle cx="21" cy="21" r="21" fill="#6cbf45"/><path d="M17,30 C13,24 21,20 17,12 M22,31 C18,24 26,20 22,11 M27,30 C23,24 31,20 27,13" fill="none" stroke="#fff" stroke-width="1.5"/></svg>
    Odor<br>Control</div>
  <div class="abs feature" style="left:489px;">
    <svg width="42" height="42" viewBox="0 0 42 42"><circle cx="21" cy="21" r="21" fill="#6cbf45"/><path d="M21,10 C26,17 28,20 28,23 A7,7 0 0 1 14,23 C14,20 16,17 21,10 Z" fill="none" stroke="#fff" stroke-width="1.5"/><path d="M11,32 Q16,29 21,32 T31,32" fill="none" stroke="#fff" stroke-width="1.5"/></svg>
    Natural<br>Absorption</div>
  <div class="abs feature" style="left:556px;">
    <svg width="42" height="42" viewBox="0 0 42 42"><circle cx="21" cy="21" r="21" fill="#6cbf45"/><path d="M11,24 L11,31 L31,31 L31,24 M11,24 L17,24 L21,28 L25,24 L31,24 M21,12 L21,24 M17,16 L21,12 L25,16" fill="none" stroke="#fff" stroke-width="1.5"/></svg>
    Interlocking<br>Trays</div>

  <h2 class="abs vet">Veterinarian Approved</h2>
  <p class="abs made">Made in</p>
  <div class="abs flag" role="img" aria-label="United States flag"></div>

  <div class="abs order" style="left:91px;">Order from Riverstore<small>riverstore</small></div>
  <div class="abs or">OR</div>
  <div class="abs order" style="left:383px;">Order from BuildMart</div>

  <div class="abs seal" role="img" aria-label="Quality seal"></div>

  <div class="abs brand footer-brand"><span class="brand-dot"></span>PawPatch Turf</div>
  <div class="abs social" style="left:127px;" role="img" aria-label="Social profile"></div>
  <div class="abs social" style="left:155px;" role="img" aria-label="Social profile"></div>
  <div class="abs social" style="left:183px;" role="img" aria-label="Social profile"></div>

  <h3 class="abs foot-head" style="left:299px;">OVERVIEW</h3>
  <ul class="abs foot-links"><li>About Us</li><li>Products</li><li>Order</li><li>Customer Service</li></ul>

  <h3 class="abs foot-head" style="left:429px;">JOIN OUR NEWSLETTER</h3>
  <p class="abs news-text">Get our latest news &amp; offers delivered to your inbox.</p>
  <div class="abs email">Enter your email address</div>
  <div class="abs subscribe">Subscribe</div>

  <div class="abs rule"></div>
  <p class="abs copyright">© Copyright 2020 PawPatch Turf. All Rights Reserved</p>
</body>
</html>
```